Zielgruppe
Wir bieten mit unserem Produkt Portix©:
1. Die kostenfreie individuelle Erstellung einer eigenständigen "mobilen Unternehmens-Webseitenversion", optimiert zur Anzeige auf Smartphones. Diese kostenfreie Erstellung erfolgt inkl. Übernahme der Seiteninhalte sowie nach dem Farbdesign der bereits bestehenden Standard-Webseiten des Kunden.
2. Das Serverhosting und Aktualisierungsservice der mobilen Unternehmens Webseitenversion des Kunden, gestaffelt nach unserer Preisliste
Zielgruppe: Unternehmen und Webseitenbetreiber ohne aktuell vorhandene mobile Unternehmens-Webseitenversion.
Unsere eigene Produkt-Webseite steht unter www.talvo-portix.de zur Ansicht bereit. Die auf unserer Webseite verwendeten Grafiken sind derzeit nur für die Onlineverwendung lizensiert. Generell könnten Grafiken von Bildquell genutzt werden. Diese könnten bei Erwerb des Projektes durch uns dann nachträglich erworben werden.
Das Design sollte grundsätzlich in den Farben unserer Produkt-Webseite (www.talvo-portix.de) umgesetzt werden.
Zukünftig: Später ist, ggfl. in Form von Zusatzaufträgen geplant, das grundsätzlich hier entstehende Design in geänderter/angepasster Farbvariation auch für andere Produkte unseres Unternehmens zu übernehmen. (So zum Beispiel die spätere Farbanpassung auf blau und angepassten Produkt-Informationen für unser Produkt RamBeQu©-Fensterpreisrechner unter: www.rambequ.de.) Gleiches oder ähnliches Flyerdesign, jedoch mit anderem Produktbild und anderen Texten soll dann einen gewissen Wiedererkennungswert unseres Unternehmens erkennen lassen.
Aufgabenstellung
Wir wünschen uns in erster Linie vor allem ein technisch-modernes Design, da gerade mobile Webseitenversionen auf technologisch moderne Endgeräte zugeschnitten sind. Die Flyer sind als Beilage für ein Briefmarketing an Unternehmen vorgesehen. Hochformat (es sei denn, hier überzeugt uns ein Designvorschlag im Querformat ;-)) 4-seitig, 100mm x 210mm Vorschläge sind willkommen - wir wissen, dass zu enge Vorgaben die Kreativität auch einengen können...
Vorschlag:
Frontseite:
Produkt-Bezeichnung: "Portix@"
Evtl. Demo-Grafik: Evtl. eine gegenüberstellende "Standard-Webseite" zur "mobile Webseinversion" auf Monitor bzw. Smartphone-Display. (siehe unsere Startseite www.talvo-portix.de)
Internetadresse: "www.talvo-portix.de"
Slogan: "Ihr Partner für mobile Webseiten"
Innenseite: (Doppelseite)
Text: "Portix© Warum eigentlich?
Smartphones liegen voll im Trend. Die Zahl mobiler Internet-Nutzer steigt und steigt.
Immer mehr Menschen surfen heute von unterwegs mit dem Smartphone. Sie sollten darauf reagieren. Mit Portix© erstellen wir Ihre smartphone-optimierte Webseitenversion nun komplett kostenfrei. Dabei übernehmen wir den Inhalt Ihrer Standard-Webseiten sowie das Farbdesign Ihres unternehmes.
Viele Unternehmen ignorieren die Anforderungen der heutigen Zeit. Die Gewinner sind innovative Unternehemen, welche ihre Kunden auch auf dem Smarthone optimal erreichen.
Wir übernehmen das für Sie..."
Darunter sollte über beide Seiten unsere Preisliste integriert werden (http://www.talvo-portix.de/portix_preise.htm)
Rückseite:
Die Rückseite sollte eine Kontakaufnahme zu uns ermöglichen.
Abtrennbar durch "Scherensymbol und Linie".
Text: "Rückantwort (Rücksendung auch per Fax möglich!)
Ich möchte das Angebot Portix© nutzen. Bitte senden Sie mir Portix©-Vertragsunterlagen zu.

```html
<!DOCTYPE html>
<html lang="de">
<head>
<meta charset="utf-8">
<title>Portix© – Innenseite Tarifübersicht</title>
<link rel="stylesheet" href="https://fonts.googleapis.com/css2?family=Open+Sans:wght@400;600;700;800&display=swap">
<style>
  :root {
    --page-bg: #eeeeee;
    --paper: #ffffff;
    --stripe-light: #a8c7a8;
    --stripe-dark: #6f9c78;
    --band-green: #3e6a4b;
    --row-green: #d6e6d6;
    --rule-white: #f4f8f4;
    --ink-green: #2c6637;
    --ink-dark: #1d1d1d;
    --tick-green: #2b6a35;
  }
  * { box-sizing: border-box; margin: 0; padding: 0; }
  html, body { width: 1200px; height: 800px; overflow: hidden; }
  body {
    background: var(--page-bg);
    font-family: "Open Sans", Verdana, sans-serif;
    position: relative;
  }
  .spread {
    position: absolute;
    left: 228px; top: 14px;
    width: 744px; height: 772px;
    background: var(--paper);
    box-shadow: 0 6px 24px rgba(0,0,0,.18);
    overflow: hidden;
  }
  .top-stripe {
    position: absolute; left: 0; top: 0; width: 100%; height: 12px;
    background: var(--stripe-light);
    border-bottom: 3px solid var(--stripe-dark);
  }
  .hero-photo {
    position: absolute; left: 371px; top: 24px; width: 373px; height: 324px;
    background: linear-gradient(135deg, #eef2f4 0%, #b9c6cf 35%, #6f7f8c 60%, #d9dfe2 100%);
  }
  .intro {
    position: absolute; left: 0; top: 24px; width: 371px; height: 324px;
    padding: 16px 20px 0 30px;
  }
  .intro-title {
    position: relative; z-index: 2;
    display: inline-block; white-space: nowrap;
    background: var(--paper);
    padding: 4px 16px 4px 0;
    font-size: 27px; line-height: 36px; font-weight: 800; color: var(--ink-green);
  }
  .intro-body {
    margin-top: 10px;
    font-size: 12.5px; line-height: 15.5px; color: var(--ink-dark);
  }
  .intro-body p + p { margin-top: 14px; }
  .intro-body strong { color: var(--ink-green); font-weight: 700; }

  .tariff { position: absolute; left: 0; top: 348px; width: 744px; }
  .tariff-row {
    display: grid;
    grid-template-columns: 371px 109px 120px 144px;
    background: var(--row-green);
    border-bottom: 3px solid var(--rule-white);
    height: 45px;
  }
  .tariff-row > div {
    display: flex; align-items: center; justify-content: center;
    border-left: 2px solid var(--rule-white);
  }
  .tariff-row > .label {
    border-left: 0;
    padding-left: 36px; padding-right: 10px;
    flex-direction: column; align-items: flex-start; justify-content: center;
    font-size: 11px; font-weight: 700; color: var(--ink-green); line-height: 12.5px;
  }
  .label small { font-weight: 400; font-size: 10.5px; }
  .tariff-head {
    background: var(--band-green); height: 44px; border-bottom: 0;
  }
  .tariff-head > div { border-left: 0; color: #fff; flex-direction: column; font-size: 11px; font-weight: 700; line-height: 12px; }
  .tariff-head > .label { color: #fff; padding-left: 36px; font-weight: 700; line-height: 11.5px; }
  .tariff-head .label span { font-weight: 400; }
  .tariff-head .label small { font-size: 7px; line-height: 9px; font-weight: 400; }
  .tariff-head .price { font-weight: 400; }
  .tariff-row.extra { margin-top: 10px; border-top: 5px solid var(--stripe-light); height: 50px; }
  .icon { width: 22px; height: 18px; }
  .fee { position: relative; }
  .fee em { position: absolute; left: 58%; top: 58%; font-style: normal; font-size: 8px; color: var(--ink-green); }
  .included { flex-direction: column; font-size: 8.5px; line-height: 9px; color: var(--ink-green); font-weight: 600; text-align: center; }
  .included .icon { opacity: .35; height: 13px; }
</style>
</head>
<body>
<svg width="0" height="0" style="position:absolute">
  <symbol id="tick" viewBox="0 0 22 18"><path d="M2 9.5 L8 15 L20 2" fill="none" stroke="#2b6a35" stroke-width="3.2" stroke-linecap="round" stroke-linejoin="round"/></symbol>
  <symbol id="cross" viewBox="0 0 22 18"><path d="M6 3 L16 15 M16 3 L6 15" fill="none" stroke="#ffffff" stroke-width="3" stroke-linecap="round"/></symbol>
</svg>

<main class="spread">
  <div class="top-stripe"></div>
  <div class="hero-photo" role="img" aria-label="Foto: Hände halten ein Smartphone vor einem Laptop"></div>

  <section class="intro">
    <h1 class="intro-title">Portix© – Warum eigentlich?</h1>
    <div class="intro-body">
      <p>Smartphones liegen voll im Trend. Die Zahl mobiler Internet-Nutzer steigt und steigt. Immer mehr Menschen surfen heute von unterwegs mit dem Smartphone. Sie sollten darauf reagieren. Mit Portix© erstellen wir Ihre smartphone-optimierte Webseitenversion nun komplett kostenfrei. Dabei übernehmen wir den Inhalt Ihrer Standard-Webseiten sowie das Farbdesign Ihres Unternehmens.</p>
      <p>Viele Unternehmen ignorieren die Anforderungen der heutigen Zeit. Die Gewinner sind innovative Unternehemen, welche ihre Kunden auch auf dem Smartphone optimal erreichen. <strong>Wir übernehmen das für Sie…</strong></p>
    </div>
  </section>

  <section class="tariff">
    <div class="tariff-row tariff-head">
      <div class="label">Portix©-Tarifübersicht <span>und Funktionsumfang /Stand 2014</span><small>(alle Preise zzgl. ges. MwSt.)</small></div>
      <div>Portix© Basis<span class="price">9,99 €/Monat</span></div>
      <div>Portix©+Install<span class="price">9,99 €/Monat</span></div>
      <div>Portix©+Admin<span class="price">14,99 €/Monat</span></div>
    </div>
    <div class="tariff-row">
      <div class="label">Einmalige Einrichtungsgebühr</div>
      <div><svg class="icon"><use href="#cross"/></svg></div>
      <div class="fee"><svg class="icon"><use href="#tick"/></svg><em>49,-€</em></div>
      <div class="fee"><svg class="icon"><use href="#tick"/></svg><em>49,-€</em></div>
    </div>
    <div class="tariff-row">
      <div class="label">Kostenfreie Erstellung Ihrer mobilen Webseiten<small>inkl. Übernahme von bisherigen Webseiteninhalten, max 10 Schaltflächen</small></div>
      <div><svg class="icon"><use href="#tick"/></svg></div>
      <div><svg class="icon"><use href="#tick"/></svg></div>
      <div><svg class="icon"><use href="#tick"/></svg></div>
    </div>
    <div class="tariff-row">
      <div class="label">Integriertes Kontaktformular</div>
      <div><svg class="icon"><use href="#tick"/></svg></div>
      <div><svg class="icon"><use href="#tick"/></svg></div>
      <div><svg class="icon"><use href="#tick"/></svg></div>
    </div>
    <div class="tariff-row">
      <div class="label">Farbanpassung an Ihre bereits bestehenden Standard-Webseiten</div>
      <div><svg class="icon"><use href="#tick"/></svg></div>
      <div><svg class="icon"><use href="#tick"/></svg></div>
      <div><svg class="icon"><use href="#tick"/></svg></div>
    </div>
    <div class="tariff-row">
      <div class="label">Installation und Freischaltung der Erkennungsweiche auf Ihrem Server</div>
      <div><svg class="icon"><use href="#cross"/></svg></div>
      <div><svg class="icon"><use href="#tick"/></svg></div>
      <div><svg class="icon"><use href="#tick"/></svg></div>
    </div>
    <div class="tariff-row">
      <div class="label">Schritt-für Schritt Installationsanleitung<small>(nur bei eigener Installation Portix© Basis)</small></div>
      <div><svg class="icon"><use href="#tick"/></svg></div>
      <div class="included"><svg class="icon"><use href="#tick"/></svg>Installation<br>inklusive</div>
      <div class="included"><svg class="icon"><use href="#tick"/></svg>Installation<br>inklusive</div>
    </div>
    <div class="tariff-row">
      <div class="label">Eigener Admin-Zugang zur eigenständigen Bearbeitung Ihrer mobilen Webseiten</div>
      <div><svg class="icon"><use href="#cross"/></svg></div>
      <div><svg class="icon"><use href="#cross"/></svg></div>
      <div><svg class="icon"><use href="#tick"/></svg></div>
    </div>
    <div class="tariff-row extra">
      <div class="label">Kostenfreie Kunden-Hotline und technischer Support</div>
      <div><svg class="icon"><use href="#cross"/></svg></div>
      <div><svg class="icon"><use href="#cross"/></svg></div>
      <div><svg class="icon"><use href="#tick"/></svg></div>
    </div>
  </section>
</main>
</body>
</html>
```